Divi Theme Wordpress Web Design

Hi,

We have had a Divi theme website running on Wordpress for a few years but need a fresh refresh.

Designs must be possible with standard Divi theme and minimal/no CSS customisation or similar. if this is required please note this in submission. Also, please note mobile and device usage which must be universal.

We have our logo files attached, plus some research and sample sites we have done, plus all of our current collateral. We will need a few examples such as landing (main) page, single blog post and software specific page. See current examples below:

Landing (Main) - http://www.vantrelworks.com/inventory-wholesale-manufacturing/

Single Blog Post - http://www.vantrelworks.com/why-remote-work-made-break-most-relaxing-ever/

Software Page - http://www.vantrelworks.com/software-implementation/plume-stockroom-implementation-and-training/

Target Market(s)

small businesses, small business owners, people who need simple but technical computer help,

Industry/Entity Type

Professional Service

Number of Pages Required

3 page

Requirements
Must have
• see attachment guide
Nice to have
• see attachment guide

```html
<!DOCTYPE html>
<html lang="en">
<head>
<meta charset="utf-8">
<title>VantrelWorks</title>
<link rel="stylesheet" href="https://fonts.googleapis.com/css2?family=Lato:ital,wght@0,400;0,700;0,900;1,400&display=swap">
<style>
:root{
  --teal:#1d5675;
  --teal-dark:#163f57;
  --teal-light:#2b9cad;
  --orange:#ef7c2a;
  --red:#8c1a22;
  --ink:#2b2b2b;
  --muted:#6b6b6b;
  --grey-band:#ececec;
  --footer:#111;
  --white:#fff;
}
*{box-sizing:border-box;margin:0;padding:0}
html,body{width:1200px;height:2628px;overflow:hidden;background:var(--white);font-family:'Lato',Arial,sans-serif;color:var(--ink)}
.page{position:relative;width:1200px;height:2628px}
section,header,footer{position:absolute;left:0;width:1200px}
.abs{position:absolute}

/* header */
.site-header{top:0;height:131px;border-top:3px solid var(--teal)}
.topbar{height:93px;background:var(--white)}
.contact-pill{position:absolute;top:30px;display:flex;align-items:center;gap:10px;font-size:14px;color:var(--ink)}
.icon-dot{width:36px;height:36px;border-radius:50%;background:var(--teal);display:flex;align-items:center;justify-content:center}
.search-dot{position:absolute;left:1000px;top:30px;width:38px;height:38px;border-radius:50%;background:var(--teal);display:flex;align-items:center;justify-content:center}
.v-sep{position:absolute;left:978px;top:26px;width:1px;height:44px;background:#ccc}
.navbar{position:absolute;top:93px;height:35px;width:1200px;background:var(--teal)}
.nav-item{position:absolute;top:0;height:35px;line-height:35px;font-size:12px;color:var(--white);text-transform:uppercase;letter-spacing:.3px}
.nav-item.active{background:var(--orange);padding:0 24px}
.nav-sep{position:absolute;top:10px;width:1px;height:15px;background:rgba(255,255,255,.35)}
.brand-tab{position:absolute;left:166px;top:6px;width:194px;height:118px;background:var(--white);border-radius:0 0 18px 18px;display:flex;flex-direction:column;align-items:center;justify-content:flex-end;padding-bottom:20px;gap:8px}
.brand-mark{width:40px;height:40px;border-radius:50%;background:var(--teal-light)}
.brand-name{font-size:27px;font-weight:700;color:var(--teal)}

/* hero */
.hero{top:131px;height:489px;background:radial-gradient(ellipse at 40% 50%,#2a4756 0%,#15232c 60%,#0e1820 100%)}
.hero-devices{position:absolute;left:163px;top:79px;width:467px;height:350px;border-radius:8px;background:linear-gradient(160deg,#d8dde0,#7f8a90 60%,#2f3a40)}
.hero-copy{position:absolute;left:600px;top:168px;width:437px;text-align:right;font-size:23px;line-height:34px;color:var(--white)}

/* shared headings */
.section-title{font-size:28px;font-weight:900;color:var(--teal);text-transform:uppercase}
.section-title .accent{color:var(--orange)}
.title-rule{position:absolute;height:2px;background:#d6d6d6}
.rule-pin{position:absolute;width:10px;height:10px;background:#bbb;border-radius:2px}

/* about */
.about{top:620px;height:288px}
.about-mark{position:absolute;left:183px;top:54px;width:180px;height:180px;border-radius:50%;background:var(--grey-band);display:flex;align-items:center;justify-content:center;font-size:22px;font-weight:700;color:var(--teal)}
.about-divider{position:absolute;left:406px;top:44px;width:2px;height:200px;background:#d0d0d0}
.about-body{position:absolute;left:457px;top:118px;width:580px;font-size:12px;line-height:21px;color:var(--muted)}
.btn{position:absolute;left:457px;top:212px;height:32px;padding:0 16px;background:var(--teal);color:var(--white);font-size:12px;font-weight:700;line-height:32px;text-transform:uppercase}

/* trust */
.trust{top:908px;height:395px;background:linear-gradient(135deg,#f2f2f2,#e2e2e2 50%,#eeeeee)}
.question{position:absolute;width:320px}
.question h3{font-size:17px;font-weight:700;color:var(--ink);margin-bottom:8px}
.question p{font-size:12px;line-height:18px;color:var(--muted)}
.question .more{display:block;margin-top:4px;font-size:12px;color:var(--orange)}
.q-left{left:142px;text-align:right}
.q-right{left:738px;text-align:left}
.q-circle{position:absolute;width:102px;height:102px;border-radius:50%;display:flex;align-items:center;justify-content:center;border:6px solid rgba(255,255,255,.7)}

/* process */
.process{top:1303px;height:435px}
.step{position:absolute;top:150px;width:180px;text-align:center}
.step-ring{width:124px;height:124px;margin:0 auto;border-radius:50%;background:var(--white);box-shadow:0 0 0 1px #e3e3e3;display:flex;align-items:center;justify-content:center}
.step-core{width:110px;height:110px;border-radius:50%;background:var(--teal);display:flex;align-items:center;justify-content:center}
.step h4{margin-top:20px;font-size:16px;font-weight:400;color:var(--ink)}
.step p{margin-top:10px;font-size:12px;line-height:18px;color:var(--muted)}

/* blog + testimonial */
.stories{top:1738px;height:350px;background:var(--grey-band)}
.pager{position:absolute;display:flex;gap:4px}
.pager span{width:20px;height:20px;border-radius:50%;border:1.5px solid var(--teal);display:flex;align-items:center;justify-content:center}
.post{position:absolute;left:161px;width:410px}
.post-thumb{position:absolute;left:0;top:0;width:114px;height:79px}
.post h5{position:absolute;left:137px;top:2px;width:280px;font-size:14px;font-weight:700}
.post p{position:absolute;left:137px;top:26px;width:280px;font-size:12px;line-height:19px;color:var(--muted)}
.post p b{color:var(--teal);font-weight:400}
.col-divider{position:absolute;left:601px;top:60px;width:1px;height:230px;background:#d0d0d0}
.avatar{position:absolute;left:629px;top:118px;width:84px;height:84px;border-radius:50%;border:3px solid var(--teal);background:linear-gradient(#c9b8a6,#6f655c)}
.author{position:absolute;left:625px;top:208px;font-size:12px;font-weight:700;color:var(--teal)}
.quote{position:absolute;left:732px;top:118px;width:305px;font-size:12px;font-style:italic;line-height:22px;color:var(--ink)}
.quote .mark{font-size:34px;color:#c6c6c6;line-height:0;vertical-align:-12px}

/* partners */
.partners{top:2088px;height:239px}
.partner{position:absolute;top:123px;width:163px;height:70px;border:1px solid #d8d8d8;display:flex;align-items:center;justify-content:center;font-size:18px;font-weight:700;color:#333}

/* footer */
.site-footer{top:2327px;height:263px;background:var(--footer);color:var(--white)}
.f-col{position:absolute;top:36px}
.f-col h6{font-size:14px;font-weight:700;text-transform:uppercase;padding-bottom:10px;border-bottom:1px solid #444;width:210px}
.f-links{list-style:none;margin-top:12px}
.f-links li{font-size:12px;line-height:33px;text-transform:uppercase}
.f-links li::before{content:"";display:inline-block;width:4px;height:4px;background:#aaa;margin-right:8px;vertical-align:3px}
.f-contact{margin-top:12px;font-size:12px;line-height:18px;color:#ddd}
.f-contact strong{display:block;font-size:15px;color:var(--white);margin-top:6px}
.map{position:absolute;left:606px;top:77px;width:263px;height:154px;background:linear-gradient(135deg,#cfe3ea,#e9e4d4 55%,#b9d5dd)}
.f-brand{position:absolute;left:893px;top:80px;width:140px;text-align:center}
.f-brand .dot{width:44px;height:44px;border-radius:50%;background:#777;margin:0 auto 8px}
.f-brand span{font-size:20px;font-weight:700;color:#ddd}
.socials{display:flex;gap:8px;justify-content:center;margin-top:14px}
.socials i{width:20px;height:20px;border-radius:50%;display:block}
.copyright{position:absolute;top:2590px;left:0;width:1200px;height:38px;background:var(--teal);color:var(--white);font-size:12px;line-height:38px;text-align:center}
</style>
</head>
<body>
<div class="page">

<header class="site-header">
  <div class="topbar">
    <div class="contact-pill" style="left:578px">
      <span class="icon-dot"><svg width="16" height="16" viewBox="0 0 24 24"><path fill="#fff" d="M6.6 10.8a15 15 0 006.6 6.6l2.2-2.2c.3-.3.7-.4 1-.2 1.1.4 2.3.6 3.6.6.6 0 1 .4 1 1V20c0 .6-.4 1-1 1A17 17 0 013 4c0-.6.4-1 1-1h3.5c.6 0 1 .4 1 1 0 1.3.2 2.5.6 3.6.1.3 0 .7-.2 1z"/></svg></span>
      +61 3 9000 4120
    </div>
    <div class="contact-pill" style="left:745px">
      <span class="icon-dot"><svg width="16" height="16" viewBox="0 0 24 24"><path fill="#fff" d="M3 5h18v14H3z"/><path fill="none" stroke="#1d5675" stroke-width="2" d="M3 6l9 7 9-7"/></svg></span>
      enquiries@vantrelworks.com
    </div>
    <div class="v-sep"></div>
    <div class="search-dot"><svg width="16" height="16" viewBox="0 0 24 24"><circle cx="10" cy="10" r="6" fill="none" stroke="#fff" stroke-width="3"/><path d="M15 15l6 6" stroke="#fff" stroke-width="3"/></svg></div>
  </div>
  <nav class="navbar">
    <span class="nav-item active" style="left:390px">Home</span>
    <span class="nav-item" style="left:505px">About Us</span>
    <span class="nav-sep" style="left:590px"></span>
    <span class="nav-item" style="left:630px">Software Solutions</span>
    <span class="nav-sep" style="left:788px"></span>
    <span class="nav-item" style="left:830px">Blog</span>
    <span class="nav-sep" style="left:888px"></span>
    <span class="nav-item" style="left:928px">Contact Us</span>
  </nav>
  <div class="brand-tab"><span class="brand-mark"></span><span class="brand-name">VantrelWorks</span></div>
</header>

<section class="hero">
  <div class="hero-devices" role="img" aria-label="Laptop, tablets and phone showing inventory dashboard screens"></div>
  <p class="hero-copy">Our Ledgerly Add-On Solutions help ambitious businesses who want to take control of their inventory by removing the guess work and enabling them to make better decisions.</p>
</section>

<section class="about">
  <div class="about-mark">VantrelWorks</div>
  <div class="about-divider"></div>
  <h2 class="section-title abs" style="left:457px;top:42px">About <span class="accent">Us</span></h2>
  <div class="title-rule" style="left:457px;top:94px;width:580px"></div>
  <div class="rule-pin" style="left:459px;top:89px"></div>
  <p class="about-body">Lorem ipsum dolor sit amet, consectetuer adipiscing elit, sed diam nonummy nibh euismod tincidunt ut laoreet dolore magna aliquam erat volutpat. Ut wisi enim ad minim veniam, quis nostrud exerci tation ullamcorper suscipit lobortis nisl ut aliquip ex ea commodo consequat. Duis autem vel eum iriure dolor in hendrerit in vulputate velit esse molestie consequat, vel illum dolore eu feugiat nulla facilisis.</p>
  <span class="btn">Read More &#9656;</span>
</section>

<section class="trust">
  <h2 class="section-title abs" style="left:0;width:1200px;text-align:center;top:38px">Do you really <span class="accent">trust your system?</span></h2>
  <div class="title-rule" style="left:161px;top:88px;width:878px"></div>
  <div class="rule-pin" style="left:595px;top:83px"></div>

  <div class="question q-left" style="top:126px"><h3>Are my employees efficient?</h3><p>Lorem ipsum dolor sit amet, consectetuer adipiscing sed diam nonummy nibh euismod tincidunt umagna .gdag aliquam erat volutpat. tincidunt ut laoreetfgf</p><span class="more">Read More &gt;&gt;</span></div>
  <div class="question q-right" style="top:126px"><h3>Are all our timesheets in for the week?</h3><p>Lorem ipsum dolor sit amet, consectetuer adipiscing sed diam nonummy nibh euismod tincidunt umagna gdag aliquam erat volutpat. tincidunt ut laoreetfgf.</p><span class="more">Read More &gt;&gt;</span></div>
  <div class="question q-left" style="top:250px"><h3>Which clients are we billing the most to?</h3><p>Lorem ipsum dolor sit amet, consectetuer adipiscing sed diam nonummy nibh euismod tincidunt umagna .gdag aliquam erat volutpat. tincidunt ut laoreetfgf</p><span class="more">Read More &gt;&gt;</span></div>
  <div class="question q-right" style="top:250px"><h3>Why did that project go over budget so quickly?</h3><p>Lorem ipsum dolor sit amet, consectetuer adipiscing sed diam nonummy nibh euismod tincidunt umagna gdag aliquam erat volutpat. tincidunt ut laoreetfgf.</p><span class="more">Read More &gt;&gt;</span></div>

  <div class="q-circle" style="left:483px;top:118px;background:var(--red)"><svg width="40" height="40" viewBox="0 0 40 40"><rect x="4" y="4" width="32" height="32" fill="none" stroke="#fff" stroke-width="2.5"/><rect x="11" y="20" width="4" height="11" fill="#fff"/><rect x="18" y="12" width="4" height="19" fill="#fff"/><rect x="25" y="16" width="4" height="15" fill="#fff"/></svg></div>
  <div class="q-circle" style="left:615px;top:118px;background:var(--teal-light)"><svg width="42" height="40" viewBox="0 0 42 40"><rect x="3" y="4" width="36" height="24" fill="none" stroke="#fff" stroke-width="2.5"/><path d="M15 36h12M21 28v8" stroke="#fff" stroke-width="2.5"/></svg></div>
  <div class="q-circle" style="left:483px;top:250px;background:var(--orange)"><svg width="40" height="40" viewBox="0 0 40 40"><path d="M4 36h32" stroke="#fff" stroke-width="2.5"/><rect x="8" y="18" width="6" height="16" fill="none" stroke="#fff" stroke-width="2.5"/><rect x="17" y="8" width="6" height="26" fill="none" stroke="#fff" stroke-width="2.5"/><rect x="26" y="14" width="6" height="20" fill="none" stroke="#fff" stroke-width="2.5"/></svg></div>
  <div class="q-circle" style="left:615px;top:250px;background:var(--teal-dark)"><svg width="40" height="40" viewBox="0 0 40 40"><rect x="5" y="5" width="30" height="22" fill="none" stroke="#fff" stroke-width="2.5"/><path d="M10 22l7-7 5 4 8-9M20 27v8M14 36l6-6 6 6" fill="none" stroke="#fff" stroke-width="2.5"/></svg></div>
  <span class="abs" style="left:590px;top:194px;width:20px;height:20px;border-radius:50%;background:var(--teal-light)"></span>
</section>

<section class="process">
  <h2 class="section-title abs" style="left:0;width:1200px;text-align:center;top:52px">Our <span class="accent">Process</span></h2>
  <div class="title-rule" style="left:161px;top:101px;width:878px"></div>
  <div class="rule-pin" style="left:595px;top:96px"></div>
  <svg class="abs" style="left:0;top:0" width="1200" height="435" viewBox="0 0 1200 435" fill="none" stroke="#777" stroke-width="1.5" stroke-dasharray="3 3">
    <path d="M285 145 Q330 110 370 128"/><path d="M364 122l8 7-10 2" stroke-dasharray="none"/>
    <path d="M645 145 Q690 110 730 128"/><path d="M724 122l8 7-10 2" stroke-dasharray="none"/>
    <path d="M465 380 Q510 410 550 363"/><path d="M543 366l8-4-1 10" stroke-dasharray="none"/>
    <path d="M825 380 Q870 410 910 363"/><path d="M903 366l8-4-1 10" stroke-dasharray="none"/>
  </svg>
  <div class="step" style="left:150px"><div class="step-ring"><div class="step-core"><svg width="52" height="52" viewBox="0 0 52 52" fill="none" stroke="#fff" stroke-width="3"><circle cx="26" cy="26" r="15"/><circle cx="26" cy="26" r="4" fill="#fff"/><path d="M26 3v12M26 37v12M3 26h12M37 26h12"/></svg></div></div><h4>Scoping</h4><p>Lorem ipsum dolor sit amet, consectetuer adipiscing sed.</p></div>
  <div class="step" style="left:330px"><div class="step-ring"><div class="step-core"><svg width="52" height="52" viewBox="0 0 52 52" fill="none" stroke="#fff" stroke-width="3"><path d="M42 20A17 17 0 0010 18M10 32a17 17 0 0032 2"/><path d="M8 10v9h9M44 42v-9h-9"/><circle cx="26" cy="26" r="7"/></svg></div></div><h4>Implementation</h4><p>Lorem ipsum dolor sit amet, consectetuer adipiscing sed.</p></div>
  <div class="step" style="left:510px"><div class="step-ring"><div class="step-core"><svg width="52" height="52" viewBox="0 0 52 52" fill="none" stroke="#fff" stroke-width="3"><path d="M12 40l4-12 22-22 8 8-22 22z"/><path d="M33 11l8 8M12 40l12-4"/></svg></div></div><h4>Training</h4><p>Lorem ipsum dolor sit amet, consectetuer adipiscing sed.</p></div>
  <div class="step" style="left:690px"><div class="step-ring"><div class="step-core"><svg width="52" height="52" viewBox="0 0 52 52"><circle cx="26" cy="26" r="15" fill="none" stroke="#fff" stroke-width="8" stroke-dasharray="6 5.8"/><circle cx="26" cy="26" r="12" fill="#fff"/><circle cx="26" cy="26" r="6" fill="#1d5675"/></svg></div></div><h4>Support ( First Month )</h4><p>Lorem ipsum dolor sit amet, consectetuer adipiscing sed.</p></div>
  <div class="step" style="left:870px"><div class="step-ring"><div class="step-core"><svg width="50" height="50" viewBox="0 0 50 50" fill="none" stroke="#fff" stroke-width="3"><rect x="7" y="10" width="36" height="32" rx="3"/><path d="M15 5v9M35 5v9"/><g fill="#fff" stroke="none"><rect x="13" y="19" width="6" height="5"/><rect x="22" y="19" width="6" height="5"/><rect x="31" y="19" width="6" height="5"/><rect x="13" y="29" width="6" height="5"/><rect x="22" y="29" width="6" height="5"/><rect x="31" y="29" width="6" height="5"/></g></svg></div></div><h4>Support ( Ongoing )</h4><p>Lorem ipsum dolor sit amet, consectetuer adipiscing sed.</p></div>
</section>

<section class="stories">
  <h2 class="section-title abs" style="left:161px;top:38px">Latest <span class="accent">Blog</span></h2>
  <div class="pager" style="left:525px;top:44px"><span><svg width="8" height="8" viewBox="0 0 8 8"><path d="M6 0L2 4l4 4" fill="none" stroke="#1d5675" stroke-width="1.5"/></svg></span><span><svg width="8" height="8" viewBox="0 0 8 8"><path d="M2 0l4 4-4 4" fill="none" stroke="#1d5675" stroke-width="1.5"/></svg></span></div>
  <div class="title-rule" style="left:161px;top:86px;width:410px"></div>
  <div class="rule-pin" style="left:163px;top:81px"></div>

  <article class="post" style="top:119px"><div class="post-thumb" role="img" aria-label="Blue glowing world map photo" style="background:linear-gradient(135deg,#0d3a6b,#3d8fd0 60%,#0c2b4f)"></div><h5>Lorem ipsum dolor sit amet, consectetuer.</h5><p>Ut wisi enim ad minim veniam, quis nostrud exerci tation ullamcorper suscipit lobortis nisl ut aliquip ex ea commodo consequat...<b>[+]</b></p></article>
  <div class="abs" style="left:161px;top:212px;width:410px;height:1px;background:#d0d0d0"></div>
  <article class="post" style="top:228px"><div class="post-thumb" role="img" aria-label="Photo of hands typing on a laptop" style="background:linear-gradient(135deg,#3b332b,#a38d6e 55%,#2a2520)"></div><h5>Lorem ipsum dolor sit amet, consectetuer.</h5><p>Ut wisi enim ad minim veniam, quis nostrud exerci tation ullamcorper suscipit lobortis nisl ut aliquip ex ea commodo consequat...<b>[+]</b></p></article>

  <div class="col-divider"></div>

  <h2 class="section-title abs" style="left:629px;top:38px">Client <span class="accent">Testimonial</span></h2>
  <div class="pager" style="left:990px;top:44px"><span><svg width="8" height="8" viewBox="0 0 8 8"><path d="M6 0L2 4l4 4" fill="none" stroke="#1d5675" stroke-width="1.5"/></svg></span><span><svg width="8" height="8" viewBox="0 0 8 8"><path d="M2 0l4 4-4 4" fill="none" stroke="#1d5675" stroke-width="1.5"/></svg></span></div>
  <div class="title-rule" style="left:629px;top:86px;width:408px"></div>
  <div class="rule-pin" style="left:631px;top:81px"></div>
  <div class="avatar" role="img" aria-label="Portrait photo of the client"></div>
  <span class="author">- Martin Ellory</span>
  <p class="quote"><span class="mark">&ldquo;</span> Lorem ipsumn sit amet co adipisclitsed udml eislimo monk dtepor incidiunt ut la dolore ma aliquanmi kn nibhn mi enim nim veni exercitation ullamco ips sdlitnol amazinl conoplk adipiscig elitsedmi do eiusmod te epo uom accuin dollarmjk oremque laudantium. Accusant doloremquenm more conmore faciles. Lorem ipsumn sit amet co adipisclitsed udml eislimo monk dtepor incidiunt ut la dolore ma aliqunmi kn nibhn mi enim nim veni exercitation ullamco ips sdlitnol amazini conoplk adipiscig elitsedmi do eiusmod. <span class="mark">&rdquo;</span></p>
</section>

<section class="partners">
  <h2 class="section-title abs" style="left:0;width:1200px;text-align:center;top:38px">Working with <span class="accent">leading lights</span></h2>
  <div class="title-rule" style="left:161px;top:88px;width:878px"></div>
  <div class="rule-pin" style="left:595px;top:83px"></div>
  <svg class="abs" style="left:126px;top:140px" width="20" height="36" viewBox="0 0 20 36"><path d="M16 2L4 18l12 16" fill="none" stroke="#ccc" stroke-width="2"/></svg>
  <svg class="abs" style="left:1053px;top:140px" width="20" height="36" viewBox="0 0 20 36"><path d="M4 2l12 16L4 34" fill="none" stroke="#ccc" stroke-width="2"/></svg>
  <div class="partner" style="left:161px">Halden HR</div>
  <div class="partner" style="left:340px">Brightmop</div>
  <div class="partner" style="left:519px">Kestrel Builders</div>
  <div class="partner" style="left:697px">Quietgate</div>
  <div class="partner" style="left:876px">Tally 365</div>
</section>

<footer class="site-footer">
  <div class="f-col" style="left:163px"><h6 style="width:145px">Quick Links</h6>
    <ul class="f-links"><li>Home</li><li>About Us</li><li>Software Solutions</li><li>Blog</li><li>Contact Us</li></ul>
  </div>
  <div class="f-col" style="left:352px"><h6 style="width:210px">Contact Information</h6>
    <div class="f-contact">
      <strong>Australia:</strong>12/48 Harbour Ln, Melbourne, VIC, 3000<br>+61 (03) 9000 4120
      <strong style="margin-top:14px">US:</strong>418 Ridgeline Parkway, Boulder, CO<br>+1 (720) 555 0142
      <div style="margin-top:16px;display:flex;align-items:center;gap:8px"><svg width="14" height="10" viewBox="0 0 14 10"><rect width="14" height="10" fill="#ddd"/><path d="M0 0l7 5 7-5" fill="none" stroke="#111" stroke-width="1.2"/></svg>enquiries@vantrelworks.com</div>
    </div>
  </div>
  <div class="f-col" style="left:606px"><h6 style="width:263px">Location Map</h6></div>
  <div class="map" role="img" aria-label="Street map with an office location pin"></div>
  <div class="f-brand"><div class="dot"></div><span>VantrelWorks</span>
    <div class="socials"><i style="background:#3b5998"></i><i style="background:#2aa3de"></i><i style="background:#d1402f"></i><i style="background:#f07e22"></i></div>
  </div>
</footer>
<div class="copyright">Copyright &copy; 2017 Vantrelworks. All Right Reserved.</div>

</div>
</body>
</html>
```